Letterhead, stationery and email signature for construction business

I need the letterhead, stationery and email signature designs for a construction business. I want them to have a corporate feel to them.

I've attached the logo for reference.

```html
<!DOCTYPE html>
<html lang="en">
<head>
<meta charset="utf-8">
<title>Halden Build – Stationery Set</title>
<link href="https://fonts.googleapis.com/css2?family=Roboto:wght@400;500;700&display=swap" rel="stylesheet">
<style>
  :root{
    --blue:#2a56a6;
    --slate:#4a4d5a;
    --ink:#33363f;
    --paper:#ffffff;
    --header-bg:#d9dadc;
    --stage-dark:#2e2f31;
    --stage-grey:#a6a6a6;
    --faint:#eef0f3;
    --divider:#d5d7dc;
  }
  *{box-sizing:border-box;margin:0;padding:0}
  html,body{width:1200px;height:2464px;overflow:hidden}
  body{position:relative;font-family:"Roboto",Arial,sans-serif;color:var(--ink);background:var(--stage-grey)}

  .brand{display:flex;align-items:center;gap:.35em;line-height:1}
  .brand-mark{width:.9em;height:.9em;background:var(--blue);flex:none}
  .brand-name{font-weight:700;color:var(--blue);letter-spacing:.02em;white-space:nowrap}
  .brand.on-blue .brand-name{color:var(--paper)}
  .brand.on-blue .brand-mark{background:var(--paper)}

  .person-name{font-weight:700;color:var(--blue);text-transform:uppercase;white-space:nowrap;line-height:1.1}
  .person-role{white-space:nowrap}

  .contact{list-style:none;display:flex;flex-direction:column}
  .contact li{display:flex;align-items:flex-start;gap:6px;white-space:nowrap;line-height:1.25}
  .contact svg{flex:none;fill:var(--blue);margin-top:.1em}

  .page-header{position:absolute;left:0;top:0;width:1200px;height:152px;background:linear-gradient(#e4e5e7,var(--header-bg));display:flex;align-items:center;justify-content:center;font-size:44px}

  .card-stage{position:absolute;left:0;top:152px;width:1200px;height:838px;background:var(--stage-dark)}
  .card{position:absolute;width:440px;height:250px;box-shadow:0 10px 24px rgba(0,0,0,.4);overflow:hidden}
  .card-back{left:130px;top:290px;background:var(--blue);display:flex;align-items:center;justify-content:center;font-size:34px}
  .card-back .faint-square{position:absolute;left:30px;top:30px;width:190px;height:190px;background:rgba(255,255,255,.05)}
  .card-front{left:630px;top:290px;background:var(--paper);border-bottom:8px solid var(--blue);display:flex;align-items:center;padding:0 24px 0 26px;gap:18px}
  .card-front .brand{font-size:18px}
  .card-front .details{border-left:1px solid var(--divider);padding-left:16px}
  .card-front .person-name{font-size:22px}
  .card-front .person-role{font-size:12px;margin:3px 0 12px}
  .card-front .contact{gap:6px;font-size:12.5px}

  .phone-screen{position:absolute;left:90px;top:1125px;width:330px;height:470px;background:radial-gradient(circle at 50% 50%,#fff 0%,#f2f2f2 45%,#cfd0d2 100%);display:flex;align-items:center;justify-content:center;font-size:30px}

  .letterhead{position:absolute;left:508px;top:1035px;width:470px;height:665px;background:var(--paper);box-shadow:0 6px 16px rgba(0,0,0,.2)}
  .letterhead .brand{position:absolute;left:20px;top:22px;font-size:18px}
  .letterhead .address{position:absolute;right:18px;top:24px;font-size:8.5px;text-align:right;display:flex;gap:6px;align-items:flex-start;line-height:1.3}
  .letterhead .faint-square{position:absolute;left:120px;top:190px;width:240px;height:240px;background:var(--faint)}
  .letterhead .contact{position:absolute;left:14px;bottom:18px;font-size:8.5px;gap:4px}
  .letterhead .rule{position:absolute;left:100px;right:0;bottom:22px;height:1px;background:var(--blue)}

  .mini-card{position:absolute;width:230px;height:142px;box-shadow:-6px 8px 16px rgba(0,0,0,.25);overflow:hidden}
  .mini-front{left:860px;top:1127px;background:var(--paper);border-bottom:3px solid var(--blue);display:flex;align-items:center;padding:0 8px 0 14px;gap:8px}
  .mini-front .brand{font-size:11px}
  .mini-front .details{border-left:1px solid var(--divider);padding-left:6px}
  .mini-front .person-name{font-size:11px}
  .mini-front .person-role{font-size:5.5px;margin:2px 0 6px}
  .mini-front .contact{font-size:5.5px;gap:3px}
  .mini-front .contact li{gap:3px}
  .mini-back{left:859px;top:1322px;background:var(--blue);display:flex;align-items:center;justify-content:flex-end;padding-right:16px;font-size:15px}
  .mini-back .faint-square{position:absolute;left:26px;top:28px;width:86px;height:86px;background:rgba(255,255,255,.05)}

  .email-signature{position:absolute;left:63px;top:1757px;width:627px;height:158px;background:var(--paper);box-shadow:0 6px 16px rgba(0,0,0,.2);padding:18px 20px}
  .email-signature .brand{font-size:22px}
  .email-signature .person-name{font-size:18px;margin-top:16px}
  .email-signature .person-role{font-size:8px;margin:2px 0 8px}
  .email-signature .contact{font-size:8.5px;gap:4px}
  .email-signature .rule{position:absolute;left:110px;right:0;bottom:16px;height:1px;background:var(--blue)}

  .compliment-slip{position:absolute;left:465px;top:1980px;width:673px;height:340px;background:var(--paper);box-shadow:0 6px 16px rgba(0,0,0,.2)}
  .compliment-slip .brand{position:absolute;left:22px;top:26px;font-size:24px}
  .compliment-slip .footer{position:absolute;left:22px;right:0;bottom:16px;display:flex;align-items:center;gap:6px;font-size:8.5px}
  .compliment-slip .footer .rule{flex:1;height:1px;background:var(--blue)}
</style>
</head>
<body>

<header class="page-header">
  <div class="brand"><span class="brand-mark"></span><span class="brand-name">HALDEN BUILD</span></div>
</header>

<section class="card-stage">
  <div class="card card-back">
    <div class="faint-square"></div>
    <div class="brand on-blue"><span class="brand-mark"></span><span class="brand-name">HALDEN BUILD</span></div>
  </div>
  <div class="card card-front">
    <div class="brand"><span class="brand-mark"></span><span class="brand-name">HALDEN BUILD</span></div>
    <div class="details">
      <p class="person-name">Mara Ellison</p>
      <p class="person-role">Chief Executive Officer</p>
      <ul class="contact">
        <li><svg width="12" height="12" viewBox="0 0 12 12"><path d="M6 0a4 4 0 0 1 4 4c0 3-4 8-4 8S2 7 2 4a4 4 0 0 1 4-4z"/></svg><span>48 Harbor Row, Suite 9<br>Austin, TX 0000</span></li>
        <li><svg width="12" height="12" viewBox="0 0 12 12"><path d="M2 0h3l1 3-2 1.5a7 7 0 0 0 3.5 3.5L9 6l3 1v3a2 2 0 0 1-2 2C4.5 12 0 7.5 0 2a2 2 0 0 1 2-2z"/></svg>555-010-2288</li>
        <li><svg width="12" height="12" viewBox="0 0 12 12"><path d="M0 2h12v8H0zM1 3l5 4 5-4" fill="none" stroke="#2a56a6" stroke-width="1.4"/></svg>info@haldenbuild.com</li>
        <li><svg width="12" height="12" viewBox="0 0 12 12"><path d="M1 1l10 4-4 1.5L5.5 11z"/></svg>HaldenBuild.com</li>
      </ul>
    </div>
  </div>
</section>

<div class="phone-screen">
  <div class="brand"><span class="brand-mark"></span><span class="brand-name">HALDEN BUILD</span></div>
</div>

<article class="letterhead">
  <div class="brand"><span class="brand-mark"></span><span class="brand-name">HALDEN BUILD</span></div>
  <p class="address"><span>48 Harbor Row, Suite 9<br>Austin, TX 0000</span><svg width="10" height="10" viewBox="0 0 12 12" fill="#2a56a6"><path d="M6 0a4 4 0 0 1 4 4c0 3-4 8-4 8S2 7 2 4a4 4 0 0 1 4-4z"/></svg></p>
  <div class="faint-square"></div>
  <ul class="contact">
    <li><svg width="9" height="9" viewBox="0 0 12 12"><path d="M2 0h3l1 3-2 1.5a7 7 0 0 0 3.5 3.5L9 6l3 1v3a2 2 0 0 1-2 2C4.5 12 0 7.5 0 2a2 2 0 0 1 2-2z"/></svg>555-010-2288</li>
    <li><svg width="9" height="9" viewBox="0 0 12 12"><path d="M0 2h12v8H0zM1 3l5 4 5-4" fill="none" stroke="#2a56a6" stroke-width="1.4"/></svg>info@haldenbuild.com</li>
    <li><svg width="9" height="9" viewBox="0 0 12 12"><path d="M1 1l10 4-4 1.5L5.5 11z"/></svg>HaldenBuild.com</li>
  </ul>
  <div class="rule"></div>
</article>

<div class="mini-card mini-front">
  <div class="brand"><span class="brand-mark"></span><span class="brand-name">HALDEN BUILD</span></div>
  <div class="details">
    <p class="person-name">Mara Ellison</p>
    <p class="person-role">Chief Executive Officer</p>
    <ul class="contact">
      <li><svg width="5" height="5" viewBox="0 0 12 12"><path d="M6 0a4 4 0 0 1 4 4c0 3-4 8-4 8S2 7 2 4a4 4 0 0 1 4-4z"/></svg><span>48 Harbor Row, Suite 9<br>Austin, TX 0000</span></li>
      <li><svg width="5" height="5" viewBox="0 0 12 12"><path d="M2 0h3l1 3-2 1.5a7 7 0 0 0 3.5 3.5L9 6l3 1v3a2 2 0 0 1-2 2C4.5 12 0 7.5 0 2a2 2 0 0 1 2-2z"/></svg>555-010-2288</li>
      <li><svg width="5" height="5" viewBox="0 0 12 12"><path d="M0 2h12v8H0zM1 3l5 4 5-4" fill="none" stroke="#2a56a6" stroke-width="1.4"/></svg>info@haldenbuild.com</li>
      <li><svg width="5" height="5" viewBox="0 0 12 12"><path d="M1 1l10 4-4 1.5L5.5 11z"/></svg>HaldenBuild.com</li>
    </ul>
  </div>
</div>
<div class="mini-card mini-back">
  <div class="faint-square"></div>
  <div class="brand on-blue"><span class="brand-mark"></span><span class="brand-name">HALDEN BUILD</span></div>
</div>

<article class="email-signature">
  <div class="brand"><span class="brand-mark"></span><span class="brand-name">HALDEN BUILD</span></div>
  <p class="person-name">Mara Ellison</p>
  <p class="person-role">Chief Executive Officer</p>
  <ul class="contact">
    <li><svg width="9" height="9" viewBox="0 0 12 12"><path d="M2 0h3l1 3-2 1.5a7 7 0 0 0 3.5 3.5L9 6l3 1v3a2 2 0 0 1-2 2C4.5 12 0 7.5 0 2a2 2 0 0 1 2-2z"/></svg>555-010-2288</li>
    <li><svg width="9" height="9" viewBox="0 0 12 12"><path d="M0 2h12v8H0zM1 3l5 4 5-4" fill="none" stroke="#2a56a6" stroke-width="1.4"/></svg>info@haldenbuild.com</li>
    <li><svg width="9" height="9" viewBox="0 0 12 12"><path d="M1 1l10 4-4 1.5L5.5 11z"/></svg>HaldenBuild.com</li>
  </ul>
  <div class="rule"></div>
</article>

<article class="compliment-slip">
  <div class="brand"><span class="brand-mark"></span><span class="brand-name">HALDEN BUILD</span></div>
  <p class="footer"><svg width="9" height="9" viewBox="0 0 12 12" fill="#2a56a6"><path d="M6 0a4 4 0 0 1 4 4c0 3-4 8-4 8S2 7 2 4a4 4 0 0 1 4-4z"/></svg><span>48 Harbor Row, Suite 9, Austin, TX 0000</span><span class="rule"></span></p>
</article>

</body>
</html>
```